Celebrate the Benefits of Creativity! Children's Dance/Creative Movement Therapist needs a rack card

We need a rack card, (4"x9"), full bleed, 4/4 for "Maple Lantern Play Collective". We offer dance and yoga classes that emphasize developmentally appropriate movement that celebrate creativity, social interaction, and the joy of self-expression. We seek to create a space for children who are not typically developing to experience the creative arts and their many benefits.
We would like to see designs that use ombre shades of purple with light orange accents. We'd like it to convey movement, connection, creativity. A bit of whimsy, perhaps, as our services are for kids! In addition to the text copy, we've uploaded 3 photo options for inclusion(anywhere from 1 - 3 may be included in the design)

```html
<!DOCTYPE html>
<html lang="en">
<head>
<meta charset="utf-8">
<title>Maple Lantern Play Collective – Rack Card</title>
<link rel="stylesheet" href="https://fonts.googleapis.com/css2?family=Montserrat:wght@700&family=Lato:wght@400;700&display=swap">
<style>
  :root {
    --orange: #f28a36;
    --plum: #6a2d5e;
    --berry-top: #a9374f;
    --berry-bottom: #7c2442;
    --white: #ffffff;
    --hands-light: #d6d6d6;
    --hands-mid: #9a9a9a;
    --hands-dark: #5c5c5c;
    --floor-light: #ecd2ac;
    --floor-mid: #d2a677;
    --floor-dark: #a86f43;
  }
  * { margin: 0; padding: 0; box-sizing: border-box; }
  html, body { width: 1200px; height: 2702px; overflow: hidden; background: var(--white); }
  .rack-card {
    position: relative;
    width: 1200px;
    height: 2702px;
    overflow: hidden;
    font-family: "Lato", sans-serif;
    color: var(--white);
  }
  .hero-photo {
    position: absolute; left: 0; top: 0; width: 1200px; height: 418px;
    background:
      radial-gradient(ellipse 60% 55% at 50% 62%, var(--hands-light), transparent 70%),
      linear-gradient(180deg, var(--hands-dark) 0%, var(--hands-mid) 55%, var(--hands-dark) 100%);
  }
  .title-band {
    position: absolute; left: 0; top: 416px; width: 1117px; height: 453px;
    background: var(--orange);
  }
  .title-accent {
    position: absolute; left: 1117px; top: 416px; width: 83px; height: 453px;
    background: var(--plum);
  }
  .title {
    position: absolute; left: 72px; top: 462px;
    font-family: "Montserrat", sans-serif; font-weight: 700;
    font-size: 118px; line-height: 115px; letter-spacing: 1px;
    text-transform: uppercase;
  }
  .story-panel {
    position: absolute; left: 0; top: 868px; width: 1200px; height: 1200px;
  }
  .story-panel svg { display: block; }
  .tagline {
    position: absolute; left: 74px; font-size: 56px; line-height: 68px; font-weight: 400;
  }
  .tagline--first { top: 961px; }
  .tagline--second { top: 1231px; }
  .intro {
    position: absolute; left: 74px; width: 1060px;
    font-size: 36px; line-height: 41px;
  }
  .intro--classes { top: 1459px; }
  .intro--mission { top: 1641px; }
  .contact {
    position: absolute; left: 74px; top: 1790px;
    font-size: 37px; line-height: 42px; font-weight: 700; font-style: normal;
  }
  .floor-photo {
    position: absolute; left: 0; top: 2030px; width: 1200px; height: 672px;
    background:
      radial-gradient(ellipse 45% 30% at 55% 55%, var(--floor-mid), transparent 75%),
      linear-gradient(180deg, var(--floor-light) 0%, var(--floor-mid) 45%, var(--floor-dark) 100%);
  }
  .social-mark {
    position: absolute; left: 292px; top: 2494px; width: 70px; height: 70px;
    background: var(--white);
  }
  .social-name {
    position: absolute; left: 74px; top: 2594px; white-space: nowrap;
    font-size: 36px; line-height: 44px;
  }
</style>
</head>
<body>
<main class="rack-card">
  <div class="hero-photo" role="img" aria-label="Black and white photo of many children's and adults' hands reaching together in a circle"></div>

  <div class="title-band"></div>
  <div class="title-accent"></div>
  <h1 class="title">Maple<br>Lantern Play<br>Collective</h1>

  <div class="floor-photo" role="img" aria-label="Photo of a dance therapist and a young girl stretching like airplanes together on a wooden studio floor"></div>

  <div class="story-panel">
    <svg width="1200" height="1200" viewBox="0 0 1200 1200" aria-hidden="true">
      <defs>
        <linearGradient id="panelOmbre" x1="0" y1="0" x2="0" y2="1">
          <stop offset="0" stop-color="var(--berry-top)"/>
          <stop offset="1" stop-color="var(--berry-bottom)"/>
        </linearGradient>
      </defs>
      <path fill="var(--orange)" d="M0 1090 H1200 V1168 C1150 1176 1110 1162 1060 1172 C1000 1184 950 1166 890 1178 C830 1190 780 1170 720 1180 C660 1192 610 1174 550 1184 C490 1194 440 1176 380 1186 C320 1196 270 1178 210 1188 C150 1198 90 1180 40 1190 L0 1192 Z"/>
      <path fill="url(#panelOmbre)" d="M0 0 H1200 V1128 C1140 1136 1100 1120 1040 1134 C980 1148 930 1126 870 1140 C810 1154 760 1130 700 1146 C640 1160 590 1136 530 1150 C470 1164 420 1140 360 1154 C300 1168 250 1142 190 1156 C130 1170 70 1146 0 1158 Z"/>
    </svg>
  </div>

  <p class="tagline tagline--first">Movement…<br>our most powerful source<br>of communication</p>
  <p class="tagline tagline--second">Connect through the power<br>of movement and mindfulness</p>

  <p class="intro intro--classes">We offer dance and yoga classes that emphasize<br>developmentally appropriate movement that celebrates<br>creativity, social interaction, and the joy of self-expression.</p>
  <p class="intro intro--mission">We seek to create a space for children who are not typically<br>developing to experience the creative arts and their many<br>benefits.</p>

  <address class="contact">
    Dana Wrenfield-Osei, M.S., R-DMT<br>
    Phone 555.014.2290<br>
    Email&nbsp; MovementWithDana@example.com
  </address>

  <span class="social-mark"></span>
  <span class="social-name">Maple-Lantern-Play-Studio</span>
</main>
</body>
</html>
```